Web design for a job listing site

We have developed a simple job listings site and need a designer to mock up a look and feel for it. We already have a logo and fonts picked out. We need design ideas for the overall look and feel as well as the header, footer and navigation elements.
The header should have our logo, a site navigation with drop-down capabilities, an account section which is a user icon that engages a drop down menu.
Bellow the header there will be the content section which will have two columns. The left section will take up 2/3 or 9 columns in a twelve column system and the right section will take up 1/3 or 3 columns.
In the left section there will be a search bar on top and listings below that very similar to http://www.bravelinkwork.com/ except we would like to appear more modern and sharp.
In the right section there will be a call to action for a new job posting at the top and an activity feed below that followed by a banner add.
Finally there is the footer which should be simple and contain copy write info and links. All content can be mocked with Lorem Ipsum.
We have attached our current logo as well as some screen grabs from the development site.
As a note the logo uses the Cinzel font which is all caps so another font must be used for the non header content. Currently we are using Droid Serif though we are open to other ideas.
Target Market(s)
We need to appeal to people looking for work and employers seeking professionals
Industry/Entity Type
Call
Colors
Designer to choose colors to be used in the design.
Look and feel

```html
<!DOCTYPE html>
<html lang="en">
<head>
<meta charset="utf-8">
<title>Greenleaf Jobs – Job Listings</title>
<link href="https://fonts.googleapis.com/css2?family=Noto+Serif:wght@400;700&display=swap" rel="stylesheet">
<style>
:root{
  --green:#6bb526;
  --green-dark:#2f6b21;
  --green-text:#5aa62a;
  --teal:#2bb3b3;
  --grey-badge:#a9a9a9;
  --page:#f0f0f0;
  --row-alt:#ebebeb;
  --line:#d6d6d6;
  --text:#444;
  --muted:#9a9a9a;
  --button:#dcdcdc;
  --footer:#6cb520;
}
*{box-sizing:border-box;margin:0;padding:0}
html,body{width:908px;height:1200px;overflow:hidden}
body{background:var(--page);font-family:"Noto Serif",serif;color:var(--text);position:relative}

.site-header{position:absolute;left:0;top:0;width:908px;height:73px;background:#fff;border-bottom:1px solid #ddd}
.brand{position:absolute;left:12px;top:22px;display:flex;align-items:center;gap:7px;font-size:20px;font-weight:700;color:var(--green-dark);letter-spacing:.5px}
.brand-mark{width:14px;height:14px;background:var(--green);border-radius:50%}
.main-nav{position:absolute;top:30px;left:365px}
.main-nav a{font-size:10.5px;text-decoration:none;color:#999;text-transform:uppercase;position:absolute;white-space:nowrap}
.main-nav a.active{color:var(--green-dark);font-weight:700}
.account{position:absolute;left:748px;top:15px;display:flex;align-items:center}
.avatar{width:42px;height:42px;border-radius:50%;background:#d4d4d4}
.account-info{margin-left:7px}
.account-name{font-size:11px;font-weight:700;color:var(--green-dark);text-transform:uppercase}
.account-links{font-size:9.5px;color:#666;margin-top:3px;display:flex;align-items:center;gap:6px}
.account-links .sep{width:1px;height:11px;background:#bbb}
.caret{width:0;height:0;border-left:4px solid transparent;border-right:4px solid transparent;border-top:4px solid #888;margin-left:4px}

.section-title{position:absolute;font-size:12.5px;color:#555;text-transform:uppercase;display:flex;align-items:center;gap:16px;white-space:nowrap}
.section-title::after{content:"";height:1px;background:var(--line);flex:1}

.search-field{position:absolute;top:137px;height:34px;background:#fff;border:1px solid #ddd;border-radius:2px;font-size:9px;color:#aaa;padding:0 15px;display:flex;align-items:center}
.search-location .divider{position:absolute;right:22px;top:8px;width:1px;height:17px;background:#ddd}
.search-location .arrow{position:absolute;right:8px;top:15px;border-left:4px solid transparent;border-right:4px solid transparent;border-top:4px solid #888}
.search-btn{position:absolute;left:526px;top:137px;width:143px;height:34px;background:var(--green);color:#fff;font-size:14.5px;font-weight:700;display:flex;align-items:center;justify-content:center;border-radius:2px;text-transform:uppercase}

.job-list{position:absolute;left:12px;top:226px;width:657px;border:1px solid #ddd;border-radius:2px;background:#fff}
.job-row{position:relative;height:67.2px;border-bottom:1px solid #ddd}
.job-row:last-child{border-bottom:none}
.job-row:nth-child(even){background:var(--row-alt)}
.badge{position:absolute;left:14px;top:15px;width:84px;height:21px;color:#fff;font-size:10px;font-weight:700;display:flex;align-items:center;justify-content:center;text-transform:uppercase;border-radius:1px}
.badge.full{background:var(--green)}
.badge.part{background:var(--grey-badge)}
.badge.commission{background:var(--teal)}
.job-title{position:absolute;left:111px;top:11px;font-size:10.5px;color:#444;text-transform:uppercase}
.job-company{position:absolute;left:111px;top:26px;font-size:9px;font-weight:700;color:var(--green-text)}
.job-poster{position:absolute;left:14px;top:44px;font-size:8.5px;color:#666;white-space:nowrap}
.job-poster b{color:#444}
.col-divider{position:absolute;top:6px;width:1px;height:55px;background:#ddd}
.job-city{position:absolute;left:365px;top:11px;font-size:10px;font-weight:700;color:var(--green-text);text-transform:uppercase}
.job-region{position:absolute;left:365px;top:26px;font-size:9px;font-weight:700;color:#666}
.job-date{position:absolute;left:545px;top:11px;font-size:10px;font-weight:700;color:var(--green-text);text-transform:uppercase}
.apply-btn{position:absolute;left:545px;top:30px;width:96px;height:22px;background:var(--button);border:1px solid #ccc;font-size:10px;color:#666;display:flex;align-items:center;justify-content:center;text-transform:uppercase}

.pagination{position:absolute;top:1070px;left:0;height:22px}
.pagination span{position:absolute;top:0;height:22px;font-size:11.5px;font-weight:700;display:flex;align-items:center;justify-content:center}
.page-nav{background:#111;color:#fff;padding:0 8px;text-transform:uppercase;gap:6px}
.page-num{width:22px;background:#a8a8a8;color:#222;border:1px solid #888}
.page-num.current{background:var(--green);color:#fff;border-color:var(--green)}

.sidebar-box{position:absolute;left:692px;width:205px;background:#e5e5e5;border-radius:2px}
.posting-box{top:111px;height:383px}
.posting-head{font-size:12.5px;font-weight:700;color:#333;padding:13px 8px 0;height:33px;border-bottom:2px solid #d0d0d0;text-transform:uppercase}
.posting-item{height:44.8px;padding:12px 8px 0;border-bottom:1px dashed #d8d8d8}
.posting-item:nth-child(odd){background:#dedede}
.posting-item .title{font-size:9.5px;font-weight:700;color:var(--green-dark);text-transform:uppercase;white-space:nowrap}
.posting-item.sales .title{color:#333}
.posting-item .place{font-size:8.5px;color:var(--green-text);margin-top:2px}
.more{position:absolute;left:92px;bottom:14px}
.banner{height:167px;display:flex;align-items:center;justify-content:center;text-align:center;font-size:29px;font-weight:700;color:#d8d8d8;line-height:1.25;text-shadow:1px 1px 0 #fff}
.banner-one{top:517px}
.banner-two{top:707px}

.site-footer{position:absolute;left:0;top:1146px;width:908px;height:54px;background:var(--footer);color:#fff;font-size:11px}
.footer-links{position:absolute;left:10px;top:20px;display:flex;gap:24px;white-space:nowrap}
.social{position:absolute;top:17px;width:20px;height:20px;background:#fff;opacity:.9;border-radius:2px}
</style>
</head>
<body>

<header class="site-header">
  <div class="brand"><span class="brand-mark"></span>GREENLEAF JOBS</div>
  <nav class="main-nav">
    <a class="active" style="left:0">Home</a>
    <a style="left:63px">Jobs</a>
    <a style="left:119px">Services</a>
    <a style="left:201px">About Us</a>
    <a style="left:285px">Contact Us</a>
  </nav>
  <div class="account">
    <div class="avatar"></div>
    <div class="account-info">
      <div class="account-name">Alex Morgan</div>
      <div class="account-links">Log out<span class="sep"></span>Setting<span class="caret"></span></div>
    </div>
  </div>
</header>

<div class="section-title" style="left:12px;top:110px;width:657px">Find the right job for you</div>
<div class="search-field search-keyword" style="left:12px;width:226px">Job Title, Skill or Company</div>
<div class="search-field search-location" style="left:246px;width:272px">Select Location<span class="divider"></span><span class="arrow"></span></div>
<div class="search-btn">Search Jobs</div>

<div class="section-title" style="left:12px;top:198px;width:657px">Recent featured jobs</div>

<section class="job-list">
  <div class="job-row"><span class="badge full">Full Time</span><span class="job-title">Assistant Teacher</span><span class="job-company">Kids Academy</span><span class="job-poster">Posted by <b>Quillmont</b></span><span class="col-divider" style="left:349px"></span><span class="job-city">Los Angeles</span><span class="job-region">California, United States</span><span class="col-divider" style="left:529px"></span><span class="job-date">5 Feb - 2015</span><span class="apply-btn">Apply Now!</span></div>
  <div class="job-row"><span class="badge part">Part-Time</span><span class="job-title">Assistant Teacher</span><span class="job-company">Kids Academy</span><span class="job-poster">Posted by <b>Quillmont</b></span><span class="col-divider" style="left:349px"></span><span class="job-city">Los Angeles</span><span class="job-region">California, United States</span><span class="col-divider" style="left:529px"></span><span class="job-date">5 Feb - 2015</span><span class="apply-btn">Apply Now!</span></div>
  <div class="job-row"><span class="badge part">Part-Time</span><span class="job-title">Assistant Teacher</span><span class="job-company">Kids Academy</span><span class="job-poster">Posted by <b>Quillmont</b></span><span class="col-divider" style="left:349px"></span><span class="job-city">Los Angeles</span><span class="job-region">California, United States</span><span class="col-divider" style="left:529px"></span><span class="job-date">5 Feb - 2015</span><span class="apply-btn">Apply Now!</span></div>
  <div class="job-row"><span class="badge full">Full Time</span><span class="job-title">Cannabis Greenhouse Handyman</span><span class="job-company">Kids Academy</span><span class="job-poster">Posted by <b>Quillmont</b></span><span class="col-divider" style="left:349px"></span><span class="job-city">Los Angeles</span><span class="job-region">California, United States</span><span class="col-divider" style="left:529px"></span><span class="job-date">5 Feb - 2015</span><span class="apply-btn">Apply Now!</span></div>
  <div class="job-row"><span class="badge commission">Commission</span><span class="job-title">Assistant Teacher</span><span class="job-company">Kids Academy</span><span class="job-poster">Posted by <b>Quillmont</b></span><span class="col-divider" style="left:349px"></span><span class="job-city">Los Angeles</span><span class="job-region">California, United States</span><span class="col-divider" style="left:529px"></span><span class="job-date">5 Feb - 2015</span><span class="apply-btn">Apply Now!</span></div>
  <div class="job-row"><span class="badge part">Part-Time</span><span class="job-title">Assistant Teacher</span><span class="job-company">Kids Academy</span><span class="job-poster">Posted by <b>Quillmont</b></span><span class="col-divider" style="left:349px"></span><span class="job-city">Los Angeles</span><span class="job-region">California, United States</span><span class="col-divider" style="left:529px"></span><span class="job-date">5 Feb - 2015</span><span class="apply-btn">Apply Now!</span></div>
  <div class="job-row"><span class="badge full">Full Time</span><span class="job-title">Assistant Teacher</span><span class="job-company">Kids Academy</span><span class="job-poster">Posted by <b>Quillmont</b></span><span class="col-divider" style="left:349px"></span><span class="job-city">Los Angeles</span><span class="job-region">California, United States</span><span class="col-divider" style="left:529px"></span><span class="job-date">5 Feb - 2015</span><span class="apply-btn">Apply Now!</span></div>
  <div class="job-row"><span class="badge commission">Commission</span><span class="job-title">Assistant Teacher</span><span class="job-company">Kids Academy</span><span class="job-poster">Posted by <b>Quillmont</b></span><span class="col-divider" style="left:349px"></span><span class="job-city">Los Angeles</span><span class="job-region">California, United States</span><span class="col-divider" style="left:529px"></span><span class="job-date">5 Feb - 2015</span><span class="apply-btn">Apply Now!</span></div>
  <div class="job-row"><span class="badge full">Full Time</span><span class="job-title">Assistant Teacher</span><span class="job-company">Kids Academy</span><span class="job-poster">Posted by <b>Quillmont</b></span><span class="col-divider" style="left:349px"></span><span class="job-city">Los Angeles</span><span class="job-region">California, United States</span><span class="col-divider" style="left:529px"></span><span class="job-date">5 Feb - 2015</span><span class="apply-btn">Apply Now!</span></div>
  <div class="job-row"><span class="badge commission">Commission</span><span class="job-title">Assistant Teacher</span><span class="job-company">Kids Academy</span><span class="job-poster">Posted by <b>Quillmont</b></span><span class="col-divider" style="left:349px"></span><span class="job-city">Los Angeles</span><span class="job-region">California, United States</span><span class="col-divider" style="left:529px"></span><span class="job-date">5 Feb - 2015</span><span class="apply-btn">Apply Now!</span></div>
  <div class="job-row"><span class="badge full">Full Time</span><span class="job-title">Assistant Teacher</span><span class="job-company">Kids Academy</span><span class="job-poster">Posted by <b>Quillmont</b></span><span class="col-divider" style="left:349px"></span><span class="job-city">Los Angeles</span><span class="job-region">California, United States</span><span class="col-divider" style="left:529px"></span><span class="job-date">5 Feb - 2015</span><span class="apply-btn">Apply Now!</span></div>
  <div class="job-row"><span class="badge commission">Commission</span><span class="job-title">Assistant Teacher</span><span class="job-company">Kids Academy</span><span class="job-poster">Posted by <b>Quillmont</b></span><span class="col-divider" style="left:349px"></span><span class="job-city">Los Angeles</span><span class="job-region">California, United States</span><span class="col-divider" style="left:529px"></span><span class="job-date">5 Feb - 2015</span><span class="apply-btn">Apply Now!</span></div>
</section>

<nav class="pagination">
  <span class="page-nav" style="left:173px;width:88px">Previous <svg width="7" height="8" viewBox="0 0 7 8"><path d="M4 0L0 4l4 4M7 0L3 4l4 4" fill="none" stroke="#888" stroke-width="1"/></svg></span>
  <span class="page-num" style="left:269px">1</span>
  <span class="page-num" style="left:299px">2</span>
  <span class="page-num current" style="left:328px">3</span>
  <span class="page-num" style="left:357px">4</span>
  <span class="page-num" style="left:387px">5</span>
  <span class="page-num" style="left:417px">6</span>
  <span class="page-nav" style="left:446px;width:61px">Next <svg width="7" height="8" viewBox="0 0 7 8"><path d="M0 0l4 4-4 4M3 0l4 4-4 4" fill="none" stroke="#888" stroke-width="1"/></svg></span>
</nav>

<aside>
  <div class="sidebar-box posting-box">
    <div class="posting-head">New Job Posting</div>
    <div class="posting-item"><div class="title">Project Officer</div><div class="place">Colorado, United States</div></div>
    <div class="posting-item"><div class="title">Project Officer</div><div class="place">Colorado, United States</div></div>
    <div class="posting-item sales"><div class="title">Regional Sales Representative</div><div class="place">Colorado, United States</div></div>
    <div class="posting-item"><div class="title">Project Officer</div><div class="place">Colorado, United States</div></div>
    <div class="posting-item sales"><div class="title">Regional Sales Representative</div><div class="place">Colorado, United States</div></div>
    <div class="posting-item"><div class="title">Project Officer</div><div class="place">Colorado, United States</div></div>
    <div class="posting-item sales"><div class="title">Regional Sales Representative</div><div class="place">Colorado, United States</div></div>
    <svg class="more" width="18" height="10" viewBox="0 0 18 10"><path d="M1 1l8 7 8-7M4 1l5 4.5L14 1" fill="none" stroke="#888" stroke-width="1"/></svg>
  </div>
  <div class="sidebar-box banner banner-one">BANNER<br>ADD</div>
  <div class="sidebar-box banner banner-two">BANNER<br>ADD</div>
</aside>

<footer class="site-footer">
  <div class="footer-links"><span>Copyright © 2014- www.greenleafjobs.example</span><span>|</span><span>Terms and Conditions</span><span>|</span><span>Privacy Policy</span></div>
  <span class="social" style="left:816px"></span>
  <span class="social" style="left:845px"></span>
  <span class="social" style="left:874px"></span>
</footer>

</body>
</html>
```